Business Recognition Design

We need a design for a recognition to be given to business leaders in our community.
The recognition shall be made on a brass plaque on wood panel background (picture attached, please use it as a background), and all drawing must be in vectors and only one color (black).
It should also have a logo on the top and signature on the right bottom.
The text is enclosed in DOC file.

Reason: just to be able to find the best solution

Reason: None of the suggestion is good enough. Logo in general is too big in comparison with the rest of the plate.

Industry/Entity Type

Business

Requirements
Must have
• - standard Windows font (or possibility to install the same font on Windows), as the name on the recognition shall be printed in the same font
Nice to have
• - some graphic element (in curves) representing achievements in business
- should look great :)

```html
<!DOCTYPE html>
<html lang="de">
<head>
<meta charset="utf-8">
<title>Auszeichnung – Kapitalwerk</title>
<link rel="stylesheet" href="https://fonts.googleapis.com/css2?family=Arimo:wght@400;700&display=swap">
<style>
  :root {
    --wood-dark: #3f2210;
    --wood-mid: #6b3d1e;
    --wood-light: #8a5530;
    --brass-deep: #b88e2c;
    --brass-mid: #d9b951;
    --brass-light: #f3e08f;
    --brass-edge: #8f6a1c;
    --ink: #111008;
    --screw-dark: #7a5a12;
    --screw-light: #f1d36a;
  }
  * { margin: 0; padding: 0; box-sizing: border-box; }
  html, body { width: 1200px; height: 919px; overflow: hidden; }
  body {
    font-family: "Arimo", Arial, sans-serif;
    color: var(--ink);
  }
  .plaque {
    position: relative;
    width: 1200px;
    height: 919px;
    background: linear-gradient(135deg, var(--wood-light) 0%, var(--wood-mid) 45%, var(--wood-dark) 100%);
  }
  .brass-plate {
    position: absolute;
    left: 47px; top: 44px;
    width: 1108px; height: 831px;
    background: linear-gradient(160deg, var(--brass-deep) 0%, var(--brass-light) 30%, var(--brass-mid) 55%, var(--brass-light) 75%, var(--brass-deep) 100%);
    border: 2px solid var(--brass-edge);
    box-shadow: 0 2px 6px rgba(0,0,0,0.5);
  }
  .screw {
    position: absolute;
    width: 22px; height: 22px;
    border-radius: 50%;
    background: radial-gradient(circle at 35% 35%, var(--screw-light) 0%, var(--brass-mid) 45%, var(--screw-dark) 100%);
    box-shadow: 0 1px 2px rgba(0,0,0,0.5);
  }
  .screw.tl { left: 78px;  top: 64px; }
  .screw.tr { left: 1101px; top: 64px; }
  .screw.bl { left: 78px;  top: 832px; }
  .screw.br { left: 1101px; top: 832px; }

  .centered { position: absolute; left: 0; width: 1200px; text-align: center; }

  .brand {
    top: 136px;
    font-size: 34px; font-weight: 700;
    display: flex; justify-content: center; align-items: center; gap: 10px;
  }
  .brand-mark { width: 18px; height: 18px; background: var(--ink); }
  .brand-rule {
    position: absolute; left: 500px; top: 186px;
    width: 202px; height: 3px; background: var(--ink);
  }
  .award-title { top: 214px; font-size: 64px; font-weight: 700; letter-spacing: 1px; }
  .award-reason { top: 306px; font-size: 44px; line-height: 55px; font-weight: 400; }
  .recipient-prefix { top: 470px; font-size: 22px; }
  .recipient-name { top: 503px; font-size: 70px; font-weight: 700; }
  .citation { top: 622px; font-size: 21.5px; line-height: 29px; }
  .citation strong { font-weight: 700; }

  .place-date {
    position: absolute; left: 190px; top: 796px; width: 290px;
    text-align: center; font-size: 22px;
  }
  .signature {
    position: absolute; left: 805px; top: 708px;
    width: 150px; height: 80px;
  }
  .signatory {
    position: absolute; left: 770px; top: 796px; width: 216px;
    text-align: center; font-size: 22px;
  }
</style>
</head>
<body>
<main class="plaque">
  <div class="brass-plate"></div>
  <span class="screw tl"></span>
  <span class="screw tr"></span>
  <span class="screw bl"></span>
  <span class="screw br"></span>

  <div class="centered brand"><span>Kapitalwerk</span><span class="brand-mark"></span></div>
  <div class="brand-rule"></div>

  <h1 class="centered award-title">AUSZEICHNUNG</h1>
  <p class="centered award-reason">als herausragendster Unternehmer<br>Deutschlands 2013</p>

  <p class="centered recipient-prefix">für Herrn Dipl.-Kfm.</p>
  <p class="centered recipient-name">Max Muster</p>

  <p class="centered citation">Unter der Leitung von Herr Dipl.-Kfm. Max Muster hat sich die <strong>FIRMA GmbH</strong> im<br>Jahr 2013 unter den ersten 5% der größten deutschen Wirtschaftsunternehmen platziert.</p>

  <p class="place-date">Gilching, 20. Juni 2013</p>
  <svg class="signature" viewBox="0 0 150 80" role="img" aria-label="Handschriftliche Unterschrift">
    <rect width="150" height="80" fill="#c9a43f" opacity="0.35"/>
  </svg>
  <p class="signatory">Clara Westfeld</p>
</main>
</body>
</html>
```